Professional looking Roller Blind Discount Card that portrays quality at a value for money price!

We need a double sided business card designed as a discount card. Size 90mm wide x 55mm high.We would like it to look professional and portray quality at a value for money price point.I have uploaded a word document with a basic layout with the information we want included on each side of the card. Please put your own thought into the layout.

Contact Information for Business Card

As per word document attached.

```html
<!DOCTYPE html>
<html lang="en">
<head>
<meta charset="utf-8">
<title>Roller Blinds Discount Card</title>
<link href="https://fonts.googleapis.com/css2?family=Bebas+Neue&family=Questrial&display=swap" rel="stylesheet">
<style>
  :root {
    --page: #ffffff;
    --card: #131313;
    --card-shape: #1c1c1c;
    --accent: #29a9e1;
    --text: #ffffff;
    --photo-brown: #6e5a51;
    --photo-frame: #1e1e1e;
  }
  * { margin: 0; padding: 0; box-sizing: border-box; }
  html, body { width: 1200px; height: 1200px; overflow: hidden; background: var(--page); }
  .canvas { position: relative; width: 1200px; height: 1200px; }
  .card {
    position: absolute; left: 178px; width: 852px; height: 473px;
    background: var(--card); overflow: hidden; color: var(--text);
    font-family: "Questrial", sans-serif;
  }
  .card--front { top: 106px; }
  .card--back { top: 628px; }
  .card__shape { position: absolute; inset: 0; width: 100%; height: 100%; }
  .offer {
    position: absolute; top: 52px; left: 0; width: 100%; text-align: center;
    font-family: "Bebas Neue", sans-serif; line-height: 1; letter-spacing: 1px;
  }
  .offer__value { font-size: 128px; }
  .offer__off { font-size: 74px; }
  .feature {
    position: absolute; top: 202px; width: 200px; margin-left: -100px;
    text-align: center; font-size: 19px; line-height: 20px; letter-spacing: 0.5px;
  }
  .feature__icon { display: block; width: 96px; height: 96px; margin: 0 auto 10px; }
  .feature--measure { left: 166px; }
  .feature--price { left: 411px; }
  .feature--family { left: 657px; }
  .feature--family .feature__text { margin-top: 6px; }
  .call {
    position: absolute; top: 390px; left: 0; width: 100%; text-align: center;
    font-family: "Bebas Neue", sans-serif; font-size: 30px; line-height: 1;
  }
  .call__number { color: var(--accent); font-size: 52px; margin: 0 6px; }
  .headline {
    position: absolute; top: 44px; left: 0; width: 100%; text-align: center;
    font-family: "Bebas Neue", sans-serif; font-size: 74px; line-height: 1; letter-spacing: 1px;
  }
  .band {
    position: absolute; top: 110px; left: 247px; width: 380px; height: 27px;
    background: var(--accent); text-align: center;
    font-size: 23px; line-height: 27px; letter-spacing: 0.5px;
  }
  .brand {
    position: absolute; top: 226px; left: 0; width: 100%; text-align: center;
    color: var(--accent); font-size: 22px; letter-spacing: 0.5px;
  }
  .tagline {
    position: absolute; top: 274px; left: 0; width: 100%; text-align: center;
    font-size: 18px; letter-spacing: 0.8px;
  }
  .gallery { position: absolute; left: 0; bottom: 0; width: 852px; height: 170px; }
</style>
</head>
<body>
<div class="canvas">

  <section class="card card--front">
    <svg class="card__shape" viewBox="0 0 852 473" aria-hidden="true">
      <path fill="var(--card-shape)" d="M160 0 H690 C800 0 880 120 820 280 C780 400 790 460 852 473 H0 C70 460 80 400 30 280 C-30 120 50 0 160 0 Z"/>
    </svg>
    <div class="offer"><span class="offer__value">25%</span><span class="offer__off">OFF</span></div>

    <div class="feature feature--measure">
      <svg class="feature__icon" viewBox="0 0 96 96" fill="var(--accent)" aria-hidden="true">
        <path d="M9 2 L17 12 H12 V56 H17 L9 66 L1 56 H6 V12 H1 Z"/>
        <path d="M46 4 L88 44 L82 50 L78 46 V68 H26 V46 L22 50 L16 44 L30 31 V8 H38 V23 Z"/>
        <rect x="44" y="46" width="16" height="22" fill="var(--card-shape)"/>
        <path d="M22 80 L32 72 V77 H82 V72 L92 80 L82 88 V83 H32 V88 Z"/>
      </svg>
      <div class="feature__text">FREE in Home<br>Measure &amp; Quote</div>
    </div>

    <div class="feature feature--price">
      <svg class="feature__icon" viewBox="0 0 96 96" aria-hidden="true">
        <path fill="var(--accent)" d="M48 2 l9 7 11-2 5 10 10 5-2 11 7 9-7 9 2 11-10 5-5 10-11-2-9 7-9-7-11 2-5-10-10-5 2-11-7-9 7-9-2-11 10-5 5-10 11 2 Z"/>
        <circle cx="48" cy="48" r="31" fill="var(--card-shape)"/>
        <path d="M33 48 L44 60 L64 35" fill="none" stroke="var(--accent)" stroke-width="8" stroke-linecap="round" stroke-linejoin="round"/>
      </svg>
      <div class="feature__text">Best Price<br>Guarantee</div>
    </div>

    <div class="feature feature--family">
      <svg class="feature__icon" viewBox="0 0 96 96" aria-hidden="true">
        <circle cx="48" cy="48" r="46" fill="var(--accent)"/>
      </svg>
      <div class="feature__text">Family Owned &amp;<br>Operated</div>
    </div>

    <div class="call">CALL<span class="call__number">0400 275 913</span>TODAY!</div>
  </section>

  <section class="card card--back">
    <svg class="card__shape" viewBox="0 0 852 473" aria-hidden="true">
      <path fill="var(--card-shape)" d="M160 0 H690 C800 0 880 120 820 280 C780 400 790 460 852 473 H0 C70 460 80 400 30 280 C-30 120 50 0 160 0 Z"/>
    </svg>
    <h1 class="headline">ROLLER BLINDS</h1>
    <div class="band">FREE in Home Measure &amp; Quote</div>
    <div class="brand">NORTHVALE PROJECTS</div>
    <div class="tagline">Huge Selection of Fabrics</div>

    <svg class="gallery" viewBox="0 303 852 170" role="img" aria-label="Photos of roller blinds fitted over sliding glass doors opening onto a leafy garden">
      <defs>
        <linearGradient id="garden" x1="0" y1="0" x2="1" y2="1">
          <stop offset="0" stop-color="#4f6a3c"/>
          <stop offset="0.5" stop-color="#6f8a5c"/>
          <stop offset="1" stop-color="#8a8a80"/>
        </linearGradient>
      </defs>
      <path fill="var(--photo-frame)" d="M102 473 C100 420 160 390 200 400 C220 360 260 340 300 360 C350 320 480 300 540 340 C570 320 610 330 640 360 C700 350 740 400 745 473 Z"/>
      <circle cx="184" cy="446" r="69" fill="var(--photo-brown)"/>
      <circle cx="239" cy="378" r="35" fill="var(--photo-brown)"/>
      <circle cx="419" cy="480" r="156" fill="url(#garden)"/>
      <circle cx="584" cy="366" r="28" fill="var(--photo-brown)"/>
      <circle cx="660" cy="436" r="66" fill="#9a9590"/>
    </svg>
  </section>

</div>
</body>
</html>
```